TEK Logistics - Banner 2.5' x 8' for 20+ locations

Need a banner designed that will pop. This banner will be displayed at over 20 of our transportation facilities. Goal is for the banner to grab the attention of employees, contractors and clients and help reinforce our mission and core values. Designed needs to include TEK Logo, our core values and mission statement. Red and Black are the main company colors and we need to stay within that theme and color pallet. Attached is a previous version that was too basic and boring. Willing to consider a design that excludes the mission statement.

Gathering more feedback

```html
<!DOCTYPE html>
<html lang="en">
<head>
<meta charset="utf-8">
<title>TEK Logistics – Core Values Banner</title>
<link href="https://fonts.googleapis.com/css2?family=Roboto+Condensed:wght@700&display=swap" rel="stylesheet">
<style>
  :root {
    --stage: #2c2a27;
    --brand-red: #d7282a;
    --ink: #111111;
    --banner-edge: #1a1a1a;
    --sky: #e6ecf5;
    --steel: #cfd4dc;
    --container-warm: #f3cdbd;
    --container-pale: #f6e6df;
  }
  * { margin: 0; padding: 0; box-sizing: border-box; }
  html, body {
    width: 1200px;
    height: 1096px;
    overflow: hidden;
    background: var(--stage);
    font-family: "Roboto Condensed", "Arial Narrow", sans-serif;
  }
  .canvas { position: relative; width: 1200px; height: 1096px; }
  .banner {
    position: absolute;
    left: 53px; top: 377px;
    width: 1094px; height: 341px;
    border: 1px solid var(--banner-edge);
    overflow: hidden;
  }
  .banner-backdrop {
    position: absolute; inset: 0;
    background: linear-gradient(100deg, var(--sky) 0%, var(--steel) 35%, var(--container-warm) 62%, var(--container-pale) 100%);
  }
  .banner-veil {
    position: absolute; inset: 0;
    background: linear-gradient(90deg, rgba(255,255,255,0.55) 0%, rgba(255,255,255,0.35) 100%);
  }
  .banner-frame {
    position: absolute;
    left: 19px; top: 17px;
    width: 1057px; height: 308px;
    border: 2px solid var(--brand-red);
  }
  .brand-name {
    position: absolute;
    left: 56px; top: 108px;
    width: 230px;
    text-align: center;
    font-size: 44px;
    font-weight: 700;
    color: var(--brand-red);
    line-height: 1;
  }
  .core-values { position: absolute; left: 0; top: 0; list-style: none; }
  .core-value {
    position: absolute;
    left: 388px;
    display: flex; align-items: center;
    font-size: 29px; font-weight: 700; color: var(--ink);
    line-height: 1; white-space: nowrap;
  }
  .core-value::before {
    content: "";
    width: 10px; height: 10px;
    border: 3px solid var(--brand-red);
    border-radius: 50%;
    margin-right: 28px;
  }
  .mission {
    position: absolute;
    left: 58px; top: 254px;
    width: 1010px;
    font-size: 26px; font-weight: 700;
    color: var(--brand-red);
    line-height: 35px;
  }
</style>
</head>
<body>
<div class="canvas">
  <section class="banner">
    <div class="banner-backdrop" role="img" aria-label="Photo of stacked shipping containers seen from below against the sky"></div>
    <div class="banner-veil"></div>
    <div class="banner-frame"></div>
    <div class="brand-name">TEK Logistics</div>
    <ul class="core-values">
      <li class="core-value" style="top:31px">Do the right things for the right reasons</li>
      <li class="core-value" style="top:67px">Pursue growth and development</li>
      <li class="core-value" style="top:103px">Build a positive team atmosphere</li>
      <li class="core-value" style="top:139px">Deliver WOW through service</li>
      <li class="core-value" style="top:176px">Do everything Safely</li>
      <li class="core-value" style="top:212px">Have Fun</li>
    </ul>
    <p class="mission">Provide the best customer experience while creating an environment of growth and opportunity for our customers, employees, and service providers.</p>
  </section>
</div>
</body>
</html>
```